Start-Up Property Development Company Requires Word Press Website Design

A new property development company in Sydney requires a new website.
This version (Version 1) is very simple and will represent one, small aspect of what the company does, which is acquiring properties for redevelopment:

Needed:
- 1 page incorporating copy, logo and illustration.
- Email contact form.
- Contact information.

It will be expanded in the next few months to include another section for marketing homes for sale (Version 2). This section should sit on top of the Version 1 (in the top section of the same scrolling page).

So this initial design must be able to simply incorporate the expansion.

The site design needs to:
- Take up the entire width of the monitor.
- Not be too different from companies corporate look and feel.
- Be simple, functional and elegant.
- Have a long scroll (1 page) with navigation items at the top of the screen simply linking to the corresponding section lower in the page.

Reason: Not happy with the choice of designs. I'm wanting something clean and fresh and not too intensive with graphics.

```html
<!DOCTYPE html>
<html lang="en">
<head>
<meta charset="utf-8">
<title>Harbourline Property – Residential &amp; Commercial Development</title>
<link href="https://fonts.googleapis.com/css2?family=Roboto+Condensed:wght@400;700&family=Arimo:wght@400;700&display=swap" rel="stylesheet">
<style>
:root{
  --red:#cf2027;
  --grey-btn:#5a5a5a;
  --icon-grey:#555;
  --teal-deep:#0d3442;
  --footer:#232323;
  --footer-line:#3a3a3a;
  --white:#fff;
  --text-muted:#666;
  --panel:rgba(40,55,62,.78);
}
*{margin:0;padding:0;box-sizing:border-box}
html,body{width:1200px;height:966px;overflow:hidden}
body{font-family:"Arimo",Arial,sans-serif;background:var(--teal-deep);position:relative}
.cond{font-family:"Roboto Condensed","Arial Narrow",sans-serif}

.hero{position:absolute;left:0;top:0;width:1200px;height:730px;
  background:
   radial-gradient(ellipse 420px 260px at 140px 160px,#2c6a93 0%,transparent 70%),
   radial-gradient(ellipse 520px 320px at 780px 560px,#8b7a63 0%,transparent 70%),
   radial-gradient(ellipse 420px 220px at 1050px 250px,#9aa3a5 0%,transparent 70%),
   linear-gradient(160deg,#2a6a98 0%,#3a7a9e 30%,#6c7c6a 55%,#8a7c68 75%,#3e6f84 100%);}
.lower-band{position:absolute;left:0;top:730px;width:1200px;height:128px;background:var(--teal-deep)}

.brand{position:absolute;left:115px;top:0;width:256px;height:101px;background:rgba(255,255,255,.85)}
.brand-mark{position:absolute;left:16px;top:16px;width:14px;height:14px;background:var(--red)}
.brand-name{position:absolute;left:38px;top:9px;font-weight:700;font-size:26px;line-height:27px;color:var(--red);white-space:nowrap}
.brand-sub{position:absolute;left:50px;top:84px;font-size:11px;color:#222;white-space:nowrap}

.top-phone{position:absolute;left:805px;top:0;width:209px;height:42px;background:rgba(255,255,255,.8);
  display:flex;align-items:center;gap:10px;padding-left:12px;font-size:24px;color:#222;white-space:nowrap}
.menu-btn{position:absolute;left:1023px;top:0;width:62px;height:42px;background:rgba(255,255,255,.8);
  display:flex;align-items:center;justify-content:center}

.welcome{position:absolute;left:218px;top:199px;width:764px;height:267px;background:var(--panel);
  color:var(--white);text-align:center}
.welcome h1{font-family:"Roboto Condensed",sans-serif;font-weight:400;font-size:35px;margin-top:13px;letter-spacing:.3px;white-space:nowrap}
.welcome h1 span{color:var(--red)}
.welcome p{font-size:15.5px;line-height:19px;margin-top:14px;padding:0 60px}
.welcome p+p{margin-top:16px;padding:0 130px}
.call-btn{position:absolute;left:265px;top:194px;width:233px;height:48px;border:1px solid rgba(255,255,255,.85);
  display:flex;align-items:center}
.call-btn .ico{width:52px;height:100%;border-right:1px solid rgba(255,255,255,.85);display:flex;align-items:center;justify-content:center}
.call-btn .num{font-family:"Roboto Condensed",sans-serif;font-size:27px;padding-left:20px;white-space:nowrap}

.card{position:absolute;top:636px;width:282px;height:191px;background:var(--white);text-align:center}
.card .badge{position:absolute;left:81px;top:-79px;width:120px;height:120px;border-radius:50%;background:#ddd;
  display:flex;align-items:center;justify-content:center}
.card .badge div{width:110px;height:110px;border-radius:50%;background:var(--icon-grey);display:flex;align-items:center;justify-content:center}
.card.accent .badge div{background:var(--red)}
.card h2{font-family:"Roboto Condensed",sans-serif;font-weight:400;font-size:21px;color:var(--icon-grey);margin-top:56px;white-space:nowrap}
.card.accent h2{color:var(--red)}
.card p{font-size:11.5px;line-height:18.5px;color:var(--text-muted);margin-top:8px;padding:0 18px}
.read-more{position:absolute;left:89px;top:146px;height:31px;width:104px;background:var(--grey-btn);color:var(--white);
  font-size:14px;line-height:31px;padding-left:9px;text-align:left;white-space:nowrap;
  clip-path:polygon(0 0,92% 0,100% 50%,92% 100%,0 100%)}
.card.accent .read-more{background:var(--red)}

.footer{position:absolute;left:0;top:858px;width:1200px;height:108px;background:var(--footer);color:var(--white);font-size:11.5px;white-space:nowrap}
.foot-nav{position:absolute;left:118px;top:11px;width:393px;height:26px;border-bottom:1px solid var(--footer-line)}
.foot-nav a{position:absolute;top:0;color:var(--white);text-decoration:none;font-size:12px}
.foot-nav a.current{color:var(--red)}
.address{position:absolute;left:119px;top:44px;letter-spacing:.5px;font-size:11px}
.contacts{position:absolute;left:119px;top:64px;height:22px;display:flex;align-items:flex-start;gap:8px;letter-spacing:.5px;font-size:11px;
  border-bottom:1px solid var(--footer-line);padding-right:20px}
.contacts svg{margin-top:2px}
.copy{position:absolute;left:122px;top:92px;font-size:12.5px;line-height:14px}
.foot-mark{position:absolute;left:612px;top:12px;width:82px;height:86px;background:#2c2c2c}
.follow{position:absolute;left:873px;top:18px;display:flex;align-items:center;gap:6px;font-family:"Roboto Condensed",sans-serif;font-size:16px}
.follow span{margin-right:6px}
.follow i{display:block;width:28px;height:28px;border-radius:50%;background:var(--white)}
.newsletter{position:absolute;left:764px;top:60px;display:flex;align-items:center;gap:6px;font-size:11.5px}
.newsletter .field{width:136px;height:26px;background:var(--white);color:#999;font-style:italic;font-size:10.5px;line-height:26px;padding-left:9px}
.newsletter .submit{width:52px;height:26px;background:var(--red);font-weight:700;font-size:13px;line-height:26px;text-align:center}
</style>
</head>
<body>
<div class="hero" role="img" aria-label="Aerial photograph of a harbour city with a bridge, waterfront and residential suburbs"></div>
<div class="lower-band"></div>

<header>
  <div class="brand">
    <i class="brand-mark"></i>
    <div class="brand-name">HARBOURLINE<br>PROPERTY</div>
    <div class="brand-sub">Residential &amp; Commerical Development</div>
  </div>
  <div class="top-phone cond">
    <svg width="28" height="28" viewBox="0 0 28 28"><circle cx="14" cy="14" r="12.5" fill="none" stroke="#cf2027" stroke-width="2"/><path d="M10 8c-1 3 0 8 5 12l2-2-2-3-2 1c-1-2-2-3-1-5l2-1-1-3z" fill="#cf2027"/></svg>
    02 9555 0142
  </div>
  <div class="menu-btn" aria-label="Menu">
    <svg width="40" height="32" viewBox="0 0 40 32" fill="#555"><circle cx="4" cy="5" r="3.5"/><rect x="10" y="2" width="29" height="6" rx="2"/><circle cx="4" cy="16" r="3.5"/><rect x="10" y="13" width="29" height="6" rx="2"/><circle cx="4" cy="27" r="3.5"/><rect x="10" y="24" width="29" height="6" rx="2"/></svg>
  </div>
</header>

<section class="welcome">
  <h1>WELCOME TO <span>HARBOURLINE</span> PROPERTY</h1>
  <p>Lorem ipsum dolor sit amet, consectetuer adipiscing elit, sed diam nonummy nibh euismod tincidunt ut laoreet dolore magna aliquam erat volutpat. Ut wisi enim ad minim veniam, quis nostrud exerci tation ullamcorper suscipit lobortis nisl</p>
  <p>So if you’re thinking of selling or interested in knowing what we think your property is worth, please contact us!</p>
  <div class="call-btn">
    <div class="ico"><svg width="30" height="30" viewBox="0 0 28 28"><circle cx="14" cy="14" r="12.5" fill="none" stroke="#fff" stroke-width="1.6"/><path d="M10 8c-1 3 0 8 5 12l2-2-2-3-2 1c-1-2-2-3-1-5l2-1-1-3z" fill="#fff"/></svg></div>
    <div class="num">02 9555 0142</div>
  </div>
</section>

<section class="card accent" style="left:142px">
  <div class="badge"><div><svg width="50" height="50" viewBox="0 0 50 50" fill="none" stroke="#fff" stroke-width="4"><path d="M30 8H8v34h34V22"/><path d="M20 32l3-9 18-18 6 6-18 18z" fill="#fff"/></svg></div></div>
  <h2>WHAT WE DO</h2>
  <p>Lorem ipsum dolor sit amet, consectetuer into euismod tincidunt ut laoreet dolore magnain aliquam erat volutpat.</p>
  <div class="read-more">READ MORE</div>
</section>

<section class="card" style="left:460px">
  <div class="badge"><div><svg width="54" height="54" viewBox="0 0 54 54" fill="#fff"><rect x="4" y="24" width="10" height="24" rx="2"/><path d="M17 24l8-12c2-4 6-3 6 1l-2 9h14c3 0 5 3 4 6l-4 16c-1 3-3 4-5 4H17z"/></svg></div></div>
  <h2>WHY CHOOSE US</h2>
  <p>Lorem ipsum dolor sit amet, consectetuer into euismod tincidunt ut laoreet dolore magnain aliquam erat volutpat.</p>
  <div class="read-more">READ MORE</div>
</section>

<section class="card" style="left:776px">
  <div class="badge"><div><svg width="58" height="58" viewBox="0 0 28 28"><circle cx="14" cy="14" r="12" fill="none" stroke="#fff" stroke-width="1.6"/><path d="M10 8c-1 3 0 8 5 12l2-2-2-3-2 1c-1-2-2-3-1-5l2-1-1-3z" fill="#fff"/></svg></div></div>
  <h2>QUICK INQUIRY</h2>
  <p>Lorem ipsum dolor sit amet, consectetuer into euismod tincidunt ut laoreet dolore magnain aliquam erat volutpat.</p>
  <div class="read-more">READ MORE</div>
</section>

<footer class="footer">
  <nav class="foot-nav">
    <a class="current" href="#" style="left:4px">Home</a>
    <a href="#" style="left:61px">About Us</a>
    <a href="#" style="left:140px">What We Do</a>
    <a href="#" style="left:237px">Services</a>
    <a href="#" style="left:317px">Contact Us</a>
  </nav>
  <div class="address">Street Name, City Name State Zip code</div>
  <div class="contacts">
    <svg width="12" height="12" viewBox="0 0 12 12" fill="#fff"><path d="M2 1l3 3-1.5 1.5c1 2 2 3 3 3L8 7l3 3-2 2C5 12 0 7 0 3z"/></svg><span>123-555-0190</span>
    <svg width="14" height="10" viewBox="0 0 14 10" fill="none" stroke="#fff" stroke-width="1.4" style="margin-left:4px"><rect x="1" y="1" width="12" height="8"/><path d="M1 1l6 5 6-5"/></svg><span>inquiry@harbourlineproperty.com</span>
  </div>
  <div class="copy">© 2014 Harbourline Property All Rights Reserved</div>
  <div class="foot-mark"></div>
  <div class="follow"><span>FOLLOW US</span><i></i><i></i><i></i><i></i></div>
  <div class="newsletter"><span>Subscribe to Newsletter</span><div class="field">email address</div><div class="submit">Submit</div></div>
</footer>
</body>
</html>
```